tri fold logistics company FLYER and A4 COMPANY FLYER COVER and A4 company flyer

we need to design company tri fold brochure and A4 company flyer cover for us
our company website is www.halvornfreight.com
pls design for us asap

ALSO OUR COMPANY NAME IS HALVORN FREIGHT INC
NOT " HALVORN FREIGHT, INC"

CAN YOU DESIGN THE COMPANY EMAIL SIGNATURE FOR US TOO

Target Market(s)

customer in U.S.

Industry/Entity Type

Freight Forwarding

Requirements
Must have
• company name and logo
• company name; HALVORN FREIGHT INC
Nice to have
• international shipping map,

```html
<!DOCTYPE html>
<html lang="en">
<head>
<meta charset="utf-8">
<title>Halvorn Freight Inc – Tri-fold Brochure</title>
<link href="https://fonts.googleapis.com/css2?family=Oswald:wght@400;500&family=Montserrat:wght@500;600;700&family=Open+Sans:wght@400;600&display=swap" rel="stylesheet">
<style>
:root{
  --stage:#5a596c;
  --paper:#ffffff;
  --ink:#3b3a45;
  --ink-soft:#6b6a75;
  --brand:#4a4370;
  --brand-deep:#3a3460;
  --lav:#e6e4ee;
  --row:#efeef4;
  --sky-top:#f6f7fb;
  --sky-mid:#c9d6e8;
  --sea:#3f8fc0;
  --cargo:#b5553e;
}
*{box-sizing:border-box;margin:0;padding:0}
html,body{width:1200px;height:1200px;overflow:hidden;background:var(--stage)}
body{font-family:"Open Sans",sans-serif;color:var(--ink);position:relative}
.spread{position:absolute;left:30px;width:1140px;height:555px;background:var(--paper);display:flex;box-shadow:0 6px 18px rgba(0,0,0,.25)}
.spread--outside{top:30px}
.spread--inside{top:615px}
.panel{position:relative;width:380px;height:100%;padding:22px 24px;border-right:1px solid #ececf2;overflow:hidden}
.panel:last-child{border-right:none}
.tag{display:inline-block;background:var(--brand);color:#fff;font-family:"Montserrat",sans-serif;font-weight:600;font-size:11px;padding:3px 10px;border-radius:0 8px 0 0;margin-bottom:8px}
p{font-size:8.6px;line-height:1.45;text-align:justify;margin-bottom:7px}
.lead{font-family:"Montserrat",sans-serif;font-weight:700;font-size:9px;color:var(--brand);margin:4px 0 4px}
ul.bullets{list-style:none;margin:0 0 8px 8px}
ul.bullets li{font-size:8.4px;line-height:1.5;padding-left:9px;position:relative}
ul.bullets li::before{content:"";position:absolute;left:0;top:5px;width:4px;height:4px;border-radius:50%;background:var(--ink)}
ul.ticks{list-style:none;margin:4px 0 10px}
ul.ticks li{font-size:8.2px;line-height:1.7;display:flex;align-items:center;gap:6px;color:var(--ink-soft)}
ul.ticks svg{flex:none}
.map{height:96px;margin:4px 0 10px;background:radial-gradient(ellipse at 40% 50%,#8fd3cc 0,#b7e4df 45%,#fff 75%)}
.contact{text-align:center;font-size:8.4px;color:var(--ink-soft)}
.contact .row{display:flex;flex-direction:column;align-items:center;gap:2px;margin-top:7px}
.partner{position:absolute;left:40px;bottom:22px;width:34px;height:24px;border-radius:4px;background:#3aa0d6}
.truck{position:absolute;left:0;right:0;bottom:0;height:92px;background:linear-gradient(180deg,#fff 0,#e7e9ef 55%,#9aa0ad 100%)}
.brandname{font-family:"Montserrat",sans-serif;font-weight:600;font-size:12px;letter-spacing:.06em;color:var(--brand-deep);display:flex;align-items:center;gap:8px}
.brandname .mark{width:18px;height:18px;border-radius:50%;background:var(--brand-deep)}
.cover-photo{position:absolute;left:0;right:0;top:70px;height:355px;background:linear-gradient(180deg,var(--sky-top) 0,var(--sky-mid) 45%,#e9eef4 62%,var(--cargo) 80%,var(--sea) 100%)}
.cover-band{position:absolute;left:0;right:0;top:425px;height:86px;background:var(--brand);color:#fff;text-align:center;padding-top:12px}
.cover-band .line1{font-family:"Montserrat",sans-serif;font-weight:500;font-size:25px}
.cover-band .line2{font-family:"Oswald",sans-serif;font-size:22px;letter-spacing:.01em}
.cover-url{position:absolute;left:0;right:0;bottom:16px;text-align:center;font-size:9px;letter-spacing:.18em;color:var(--ink-soft)}
.intro-bar{background:var(--brand);color:#fff;font-family:"Montserrat",sans-serif;font-weight:600;font-size:8.6px;padding:4px 8px;margin-bottom:6px}
.transit{width:100%;border-collapse:collapse;font-size:7.2px;margin-bottom:5px}
.transit caption{font-family:"Montserrat",sans-serif;font-weight:700;font-size:7.6px;color:var(--brand-deep);padding:1px 0}
.transit th{background:var(--brand);color:#fff;font-weight:600;text-align:left;padding:1px 4px}
.transit td{padding:0 4px;line-height:9px}
.transit tr:nth-child(even) td{background:var(--row)}
.transit td.num{text-align:center}
.carrier{position:absolute;left:0;right:0;bottom:14px;text-align:center;font-family:"Montserrat",sans-serif;font-weight:700;font-size:15px;color:#1f5fa8}
.ship-photo{position:absolute;bottom:0;background:linear-gradient(180deg,#e9eef5 0,#c7d3e2 30%,var(--cargo) 55%,#2f9fd0 80%,#86a8c4 100%)}
.ship-photo--left{left:0;right:0;height:175px}
.sky-photo{position:absolute;left:0;right:0;top:200px;bottom:0;background:linear-gradient(180deg,#fff 0,#dbe5f1 30%,#c7d3e2 55%,var(--cargo) 72%,#2f9fd0 88%,#86a8c4 100%)}
.inside-logo{position:absolute;left:60px;top:310px}
</style>
</head>
<body>

<section class="spread spread--outside" aria-label="Brochure outside">
  <article class="panel panel--about">
    <span class="tag">About Us</span>
    <p>Halvorn Freight Inc is a licensed NVOCC that specializes in air, ocean and inland transportation throughout the world. Our enthusiastic team dedicates itself to provide reliable and trustworthy service. Our team can help you choose the most efficient and economic solutions to ship your products anywhere in the world, as well as provide updates for your shipments every step of the way. Our services include but are not limited to:</p>
    <ul class="ticks">
      <li><svg width="9" height="9" viewBox="0 0 10 10"><circle cx="5" cy="5" r="4.3" fill="none" stroke="#6b6a75"/><path d="M3 5l1.5 1.5L7 3.7" fill="none" stroke="#6b6a75"/></svg>Air/Ocean Freight Forwarding</li>
      <li><svg width="9" height="9" viewBox="0 0 10 10"><circle cx="5" cy="5" r="4.3" fill="none" stroke="#6b6a75"/><path d="M3 5l1.5 1.5L7 3.7" fill="none" stroke="#6b6a75"/></svg>Inland Transportation for full truckloads and less than truckloads</li>
      <li><svg width="9" height="9" viewBox="0 0 10 10"><circle cx="5" cy="5" r="4.3" fill="none" stroke="#6b6a75"/><path d="M3 5l1.5 1.5L7 3.7" fill="none" stroke="#6b6a75"/></svg>Customs Brokerage with our own AMS system</li>
      <li><svg width="9" height="9" viewBox="0 0 10 10"><circle cx="5" cy="5" r="4.3" fill="none" stroke="#6b6a75"/><path d="M3 5l1.5 1.5L7 3.7" fill="none" stroke="#6b6a75"/></svg>Automotive shipping</li>
      <li><svg width="9" height="9" viewBox="0 0 10 10"><circle cx="5" cy="5" r="4.3" fill="none" stroke="#6b6a75"/><path d="M3 5l1.5 1.5L7 3.7" fill="none" stroke="#6b6a75"/></svg>Personal effects shipping</li>
      <li><svg width="9" height="9" viewBox="0 0 10 10"><circle cx="5" cy="5" r="4.3" fill="none" stroke="#6b6a75"/><path d="M3 5l1.5 1.5L7 3.7" fill="none" stroke="#6b6a75"/></svg>Courier services</li>
      <li><svg width="9" height="9" viewBox="0 0 10 10"><circle cx="5" cy="5" r="4.3" fill="none" stroke="#6b6a75"/><path d="M3 5l1.5 1.5L7 3.7" fill="none" stroke="#6b6a75"/></svg>Over the road cross-border shipping for Canada and Mexico</li>
    </ul>
    <div class="map" role="img" aria-label="International shipping map with route markers"></div>
    <div class="contact">
      <div>Our friendly staff is available 24 hours a day, 7 days a week, feel free to contact us:</div>
      <div class="row"><svg width="10" height="10" viewBox="0 0 10 10"><path d="M2 1l2 2-1 1.2c.6 1.3 1.5 2.2 2.8 2.8L7 6l2 2-1.2 1.3C4.5 9 1 5.5.7 2.2z" fill="none" stroke="#6b6a75" stroke-width=".9"/></svg>1-555-010-2716</div>
      <div class="row"><svg width="10" height="10" viewBox="0 0 10 10"><rect x="1.5" y="3" width="7" height="5" fill="none" stroke="#6b6a75" stroke-width=".9"/><rect x="3" y="1" width="4" height="2" fill="none" stroke="#6b6a75" stroke-width=".9"/></svg>1-555-010-2717</div>
      <div class="row"><svg width="11" height="9" viewBox="0 0 11 9"><rect x=".5" y=".5" width="10" height="8" fill="none" stroke="#6b6a75"/><path d="M.5.5l5 4 5-4" fill="none" stroke="#6b6a75"/></svg>info@halvornfreight.com</div>
      <div class="row"><svg width="10" height="10" viewBox="0 0 10 10"><circle cx="5" cy="5" r="4.3" fill="none" stroke="#6b6a75"/><path d="M.7 5h8.6M5 .7c-2.4 2.6-2.4 6 0 8.6M5 .7c2.4 2.6 2.4 6 0 8.6" fill="none" stroke="#6b6a75" stroke-width=".8"/></svg>www.halvornfreight.com</div>
    </div>
    <div class="partner" role="img" aria-label="Partner network badge"></div>
  </article>

  <article class="panel panel--domestic">
    <span class="tag">Domestic Shipping</span>
    <p>Halvorn is your one stop destination for all your domestic freight needs. We have the tools and the know-how necessary to get your freight to its destination in a timely, efficient, and affordable manner. We have built strong relationships with trucking companies across the country ensuring that we can provide you with the best rates and services.</p>
    <p>Utilizing our industry leading trucking partners, we can handle a wide range of freight from the smallest box to the heaviest load. Have any freight that needs to cross the border? Whether it's a full truckload (FTL) or less than truckload (LTL) our carriers provide seamless solutions for delivery into Canada or Mexico.</p>
    <div class="lead">Our most common over the road services include:</div>
    <ul class="bullets">
      <li>FTL (Full Truck Load)</li>
      <li>LTL (Less-than-Truck Load)</li>
      <li>Temperature Controlled Transportation</li>
      <li>Oversized loads (Flat Beds, Low boys, etc.)</li>
      <li>Expedited or 'hot shot' delivery</li>
    </ul>
    <span class="tag">FBA Forwarding Services</span>
    <p>Halvorn Freight can provide you with a full tailored service for your FBA (Fulfillment by Marketbay) business. From manufacturer to the warehouse we offer a fully custom solution guaranteed to get your products where you need them, on time, and within budget. Every order will be handled personally by one of our Import/Export coordinators.</p>
    <ul class="bullets">
      <li>Ocean and Air Freight: From your shipper to the United States</li>
      <li>Customs Clearance: Into the United States</li>
      <li>Domestic Trucking: To Marketbay's warehouse</li>
      <li>Labeling: Ensuring proper labeling</li>
      <li>Warehousing-Duty</li>
      <li>Quality Assurance / Control</li>
    </ul>
    <div class="truck" role="img" aria-label="Company branded freight truck on the road"></div>
  </article>

  <article class="panel panel--cover">
    <div class="brandname"><span class="mark"></span>HALVORN FREIGHT INC</div>
    <div class="cover-photo" role="img" aria-label="Airliner climbing above a container ship in port"></div>
    <div class="cover-band">
      <div class="line1">Your solution to</div>
      <div class="line2">ALL YOUR SHIPPING NEEDS</div>
    </div>
    <div class="cover-url">www.halvornfreight.com</div>
  </article>
</section>

<section class="spread spread--inside" aria-label="Brochure inside">
  <article class="panel panel--transit">
    <div class="intro-bar">When your shipment is too big to fly but also pressing enough that time is a significant factor, this service is for you.</div>
    <p>We offer an expedited transpacific express service for full container loads from Shanghai, Ningbo or Xiamen to select US markets. The expedited service is designed for customers looking for fast, reliable ocean transit times to the U.S. West Coast and select inland locations.</p>
    <div class="intro-bar">Expedited service transit times from China</div>
    <table class="transit">
      <caption>FROM SHANGHAI</caption>
      <tr><th>Destination City</th><th>Port to Port</th><th>Port to Railyard</th></tr>
      <tr><td>Long Beach</td><td class="num">10 days</td><td></td></tr>
      <tr><td>Atlanta, GA · Chicago, IL</td><td></td><td class="num">19 / 16 days</td></tr>
      <tr><td>St. Louis, MO · South Kearny, NJ</td><td></td><td class="num">19 / 21 days</td></tr>
      <tr><td>Philadelphia, PA · Memphis, TN</td><td></td><td class="num">24 / 17 days</td></tr>
      <tr><td>Dallas, TX · Houston, TX</td><td></td><td class="num">17 / 18 days</td></tr>
      <tr><td>Honolulu</td><td class="num">17 days</td><td></td></tr>
    </table>
    <table class="transit">
      <caption>FROM NINGBO</caption>
      <tr><th>Destination City</th><th>Port to Port</th><th>Port to Railyard</th></tr>
      <tr><td>Long Beach</td><td class="num">12 days</td><td></td></tr>
      <tr><td>Atlanta, GA · Chicago, IL</td><td></td><td class="num">21 / 20 days</td></tr>
      <tr><td>St. Louis, MO · South Kearny, NJ</td><td></td><td class="num">21 / 23 days</td></tr>
      <tr><td>Philadelphia, PA · Memphis, TN</td><td></td><td class="num">22 / 20 days</td></tr>
      <tr><td>Dallas, TX · Houston, TX</td><td></td><td class="num">20 / 19 days</td></tr>
      <tr><td>Honolulu</td><td class="num">19 days</td><td></td></tr>
    </table>
    <table class="transit">
      <caption>FROM XIAMEN</caption>
      <tr><th>Destination City</th><th>Port to Port</th><th>Port to Railyard</th></tr>
      <tr><td>Long Beach</td><td class="num">14 days</td><td></td></tr>
      <tr><td>Atlanta, GA · Chicago, IL</td><td></td><td class="num">23 / 22 days</td></tr>
      <tr><td>St. Louis, MO · South Kearny, NJ</td><td></td><td class="num">23 / 25 days</td></tr>
      <tr><td>Philadelphia, PA · Memphis, TN</td><td></td><td class="num">24 / 22 days</td></tr>
      <tr><td>Dallas, TX · Houston, TX</td><td></td><td class="num">22 / 22 days</td></tr>
      <tr><td>Honolulu</td><td class="num">22 days</td><td></td></tr>
    </table>
    <div class="carrier">Corvane Line</div>
  </article>

  <article class="panel panel--ocean">
    <span class="tag">Ocean Freight Services</span>
    <p>We leverage our service contracts and strong network of more than 100 agents around the world. Effective communication and extensive experience make us one of the most reliable and professional services in the industry. We are confident that we can make shipping arrangements that are a perfect fit for your needs.</p>
    <p>We are an Ocean Transportation Intermediary (OTI) and Non-Vessel Operating Common Carrier (NVOCC) as licensed by the Federal Maritime Commission. We are also able to provide customs clearance at every US port under a licensed partner.</p>
    <div class="lead">Our most common ocean services include:</div>
    <ul class="bullets">
      <li>FCL (Full Container Load) import and export</li>
      <li>LCL (Less than Container Load) import and export</li>
      <li>General cargo or Dangerous Goods</li>
      <li>Personal effects, residential pick up or delivery</li>
      <li>Marketbay shipments importing from China</li>
    </ul>
    <div class="inside-logo brandname"><span class="mark"></span>HALVORN FREIGHT INC</div>
    <div class="ship-photo ship-photo--left" role="img" aria-label="Container ship loaded with cargo at sea"></div>
  </article>

  <article class="panel panel--air">
    <span class="tag">Air Shipments and Expedited Delivery</span>
    <p>Halvorn Freight provides international air freight services with competitive rates and reliable transit times. Our expert air team can find the best routing for your shipments whatever the size, weight or urgency.</p>
    <p>We have strategic alliances with major international airlines, allowing us to move cargo anywhere in the world. For time sensitive cargo we offer every option to help you meet your deadlines, with the fastest and most cost effective delivery options available.</p>
    <div class="sky-photo" role="img" aria-label="Airliner taking off above a container ship"></div>
  </article>
</section>

</body>
</html>
```